Kestrel - Adventurous, Fun, Exciting, Social Fitness Club needs a Biz Card/Promo Card with Attitude!

Kestrel... we're a fun, social, outdoor fitness club that needs not just a Business Card for our Trainers, but a mini-promo card that shows off our unique, innovative and cheeky personality/brand to the world!
Who Are We? We're a fun & social fitness club that prides ourselves on getting our members outdoors trying new, exciting physical activities in an effort to find joy in an active lifestyle, and sharing that experience with other like minded people. We offer:
- Personal Training (1-on-1 Fitness Training)
- Group Fitness Classes (Boxing, Pilates, etc)
- Boot Camps (Military Style - Sandbags, Ropes, Tyres, etc)
- Events (Fun Runs, Triathlons, Ocean Swims, Treks, etc)
- Adventures (Machu Picchu Trek, Rock Climbing, Kayaking, etc)
Our tag line is 'No Judgements. No Limits!' The business card should be bold, exciting, adventurous and innovative, illustrating the values of our brand: possibility, thirst for life, personal accomplishment & freedom. It should be fun, friendly & inviting... but not over the top. Think trendy surf brand style of look.
Forget your standard, boring, basic business cards that are just for contact details, our business card actually has 4 key purposes:
(1) Provide our contact details
(2) Highlight main benefits of what we do
(3) Lead generation via the offer of a Free Trial
(4) Direct people to "Like" us on Chatterbox
(see an example of business card/promo card combo attached)
THE DESIGN MUST COMPLIMENT & BE CONSISTENT IN LOOK WITH OUR NEWLY DESIGNED WEBSITE (see attached)
Look forward to seeing what you come up with! ;)

Reason: Extending by 5 days as still no design close enought to what we're after. Cheers

Industry/Entity Type
Fitness
Requirements
Must have
- - Please see attached Layout for all requirements
- Primary Colour to be orange + some limited use of darker orange shading (as per website)
- Want to see white dotted patten, dark orange "splat" (as per website).
Nice to have
- - size preference is 90 x 45mm.
Should not have
- - No rounded edges
- Only very minimal/no use of the "sun rays" effect (as used behind logo in the website design)

```html
<!DOCTYPE html>
<html lang="en">
<head>
<meta charset="utf-8">
<title>Kestrel – Trainer Business / Promo Card</title>
<link rel="stylesheet" href="https://fonts.googleapis.com/css2?family=Play:wght@400;700&family=Open+Sans:wght@600;700;800&family=PT+Sans:wght@700&family=PT+Serif&display=swap">
<style>
  :root {
    --card-orange: #c85605;
    --swirl-tone: rgba(240, 170, 50, 0.55);
    --band-dark: #231f20;
    --ink-white: #ffffff;
    --logo-yellow: #ffd21a;
    --label-slate: #33333f;
    --page-bg: #ffffff;
    --social-blue: #3b5a9a;
    --tag-shadow: #2a1306;
  }
  * { box-sizing: border-box; margin: 0; padding: 0; }
  html, body { width: 1200px; height: 900px; overflow: hidden; background: var(--page-bg); }
  .canvas { position: relative; width: 1200px; height: 900px; }

  .card {
    position: absolute; left: 22px; width: 871px; height: 420px;
    background: var(--card-orange); overflow: hidden; color: var(--ink-white);
  }
  .card--front { top: 20px; }
  .card--back { top: 455px; }

  .swirl {
    position: absolute; inset: 0;
    background:
      radial-gradient(ellipse 260px 150px at 700px 70px, var(--swirl-tone), transparent 70%),
      radial-gradient(ellipse 200px 120px at 820px 260px, rgba(240,170,50,0.35), transparent 70%);
  }
  .card--back .swirl {
    background:
      radial-gradient(ellipse 300px 140px at 250px 200px, rgba(240,150,40,0.35), transparent 70%),
      radial-gradient(ellipse 260px 160px at 700px 330px, rgba(240,150,40,0.3), transparent 70%);
  }

  .brand-name {
    position: absolute; left: 48px; top: 62px;
    font-family: "Play", sans-serif; font-weight: 700; font-size: 76px;
    letter-spacing: 4px; color: var(--logo-yellow); line-height: 1;
  }

  .trainer { position: absolute; left: 24px; top: 165px; font-family: "Play", sans-serif; font-weight: 700; letter-spacing: 1.5px; }
  .trainer__name, .trainer__role { font-size: 25px; line-height: 32px; }
  .contact { list-style: none; margin-top: 12px; }
  .contact li { font-size: 25px; line-height: 32px; }

  .services {
    position: absolute; left: 0; bottom: 0; width: 100%; height: 45px;
    background: var(--band-dark); display: flex; align-items: center; justify-content: space-between;
    padding: 0 20px;
    font-family: "Open Sans", sans-serif; font-weight: 700; font-size: 26px; letter-spacing: 0.4px;
  }

  .pitch { position: absolute; left: 26px; top: 24px; font-family: "Open Sans", sans-serif; font-weight: 600; font-size: 23px; line-height: 31px; letter-spacing: 0.3px; }
  .pitch p + p { margin-top: 17px; }

  .tagline {
    position: absolute; font-family: "Open Sans", sans-serif; font-weight: 800;
    font-size: 32px; letter-spacing: 1px; text-transform: uppercase; color: var(--ink-white);
    text-shadow: 2px 2px 0 var(--tag-shadow); white-space: nowrap; line-height: 1;
  }
  .tagline--judgements { left: 518px; top: 70px; transform: rotate(17deg); transform-origin: left center; }
  .tagline--limits { left: 503px; top: 135px; transform: rotate(17deg); transform-origin: left center; }

  .valid-box {
    position: absolute; left: 48px; top: 350px; width: 258px; height: 52px;
    background: var(--ink-white); border: 2px solid #111; color: #111;
    font-family: "PT Serif", serif; font-size: 24px; line-height: 48px; padding-left: 20px; word-spacing: 22px;
  }

  .social { position: absolute; left: 495px; top: 310px; display: flex; align-items: center; gap: 18px; }
  .social__name {
    width: 118px; height: 98px; display: flex; flex-direction: column; align-items: center; justify-content: center; gap: 6px;
    font-family: "Open Sans", sans-serif; font-weight: 700; font-size: 15px; color: var(--ink-white);
  }
  .social__mark { width: 36px; height: 36px; background: var(--social-blue); }
  .social__list { list-style: none; font-family: "Open Sans", sans-serif; font-weight: 700; font-size: 18px; line-height: 24px; }

  .side-label {
    position: absolute; left: 930px; width: 56px; text-align: center;
    font-family: "PT Sans", sans-serif; font-weight: 700; font-size: 54px; line-height: 60px; color: var(--label-slate);
  }
  .side-label--front { top: 78px; }
  .side-label--back { top: 528px; }
  .side-label span { display: block; }
</style>
</head>
<body>
<main class="canvas">

  <section class="card card--front" aria-label="Card front">
    <div class="swirl" role="img" aria-label="Faint tribal swirl decoration"></div>
    <div class="brand-name">KESTREL</div>
    <div class="trainer">
      <p class="trainer__name">Marcus Delvane</p>
      <p class="trainer__role">Director &amp; Head Personal Trainer</p>
      <ul class="contact">
        <li>P. 1300 555 204</li>
        <li>M. 0400 555 392</li>
        <li>E. marcus@kestrelfitness.com.au</li>
        <li>W. www.kestrelfitness.com.au</li>
      </ul>
    </div>
    <div class="services">
      <span>Personal Training</span>
      <span>Fitness Classes</span>
      <span>Events &amp; Adventure</span>
    </div>
  </section>

  <section class="card card--back" aria-label="Card back">
    <div class="swirl" role="img" aria-label="Faint tribal swirl decoration"></div>
    <div class="pitch">
      <p>Want to Get Fit &amp; Into Shape?<br>Let Us Show You How</p>
      <p>No Boring Workouts<br>No Long Term Contracts<br>Results Guaranteed</p>
      <p>FREE Initial Consult &amp; 30min 1- on-1<br>Session (valued $80.00)</p>
      <p>Call 1300 555 204 Now To Book</p>
    </div>
    <p class="tagline tagline--judgements">No Judgements</p>
    <p class="tagline tagline--limits">No Limits</p>
    <div class="valid-box">VALID: / /</div>
    <div class="social">
      <div class="social__name"><span class="social__mark"></span>Chatterbox</div>
      <ul class="social__list">
        <li>Join the Kestrel Online</li>
        <li>Competitions</li>
        <li>Special Deals</li>
        <li>Hints, Tips + More</li>
      </ul>
    </div>
  </section>

  <div class="side-label side-label--front"><span>F</span><span>R</span><span>O</span><span>N</span><span>T</span></div>
  <div class="side-label side-label--back"><span>B</span><span>A</span><span>C</span><span>K</span></div>

</main>
</body>
</html>
```